Property Auctions with Teodor Bramwick

Podcast cover art 3000px by 3000px. Eye catching for a weekly podcast. The words should read Property Auctions (large font) with Teodor Bramwick (smaller font)

I would like the font and colours to be similar to my book, a copy of which I have attached.

Target Market(s)

New and experienced property investors looking to purchase at a property auction

```html
<!DOCTYPE html>
<html lang="en">
<head>
<meta charset="utf-8">
<title>Property Auctions with Teodor Bramwick – Podcast Cover</title>
<link href="https://fonts.googleapis.com/css2?family=Oswald:wght@600;700&display=swap" rel="stylesheet">
<style>
  :root {
    --slate: #283337;
    --gold-dark: #a57c45;
    --gold-mid: #d2b977;
    --gold-light: #fdfcb2;
    --white: #ffffff;
    --sky: #f4f6f2;
    --grass-light: #9cc85a;
    --grass: #4f8f2a;
    --grass-deep: #2f6a1c;
  }
  html, body {
    margin: 0;
    padding: 0;
    width: 1200px;
    height: 1200px;
    overflow: hidden;
    background: var(--white);
  }
  .cover {
    position: relative;
    width: 1200px;
    height: 1200px;
    overflow: hidden;
  }
  .cover-photo {
    position: absolute;
    inset: 0;
    background:
      radial-gradient(ellipse at 85% 20%, var(--white) 0%, var(--sky) 30%, rgba(244,246,242,0) 55%),
      linear-gradient(180deg, #dfe6d8 0%, #c7d6b4 45%, var(--grass-light) 68%, var(--grass) 85%, var(--grass-deep) 100%);
  }
  .cover-art {
    position: absolute;
    inset: 0;
    width: 1200px;
    height: 1200px;
  }
  .title-line {
    font-family: "Oswald", sans-serif;
    font-weight: 700;
  }
  .host-name {
    font-family: "Oswald", sans-serif;
    font-weight: 600;
    fill: var(--white);
  }
</style>
</head>
<body>
<main class="cover">
  <div class="cover-photo" role="img" aria-label="Photo of a small wooden model house standing in fresh green grass with a soft blurred bright background"></div>
  <svg class="cover-art" viewBox="0 0 1160 1160" xmlns="http://www.w3.org/2000/svg">
    <defs>
      <linearGradient id="goldText" x1="0" y1="0" x2="1" y2="0">
        <stop offset="0" stop-color="var(--gold-dark)"/>
        <stop offset="0.5" stop-color="var(--gold-light)"/>
        <stop offset="1" stop-color="var(--gold-dark)"/>
      </linearGradient>
      <linearGradient id="goldRing" x1="0" y1="1" x2="1" y2="0">
        <stop offset="0" stop-color="var(--gold-dark)"/>
        <stop offset="0.4" stop-color="var(--gold-light)"/>
        <stop offset="0.75" stop-color="var(--gold-mid)"/>
        <stop offset="1" stop-color="var(--gold-dark)"/>
      </linearGradient>
    </defs>

    <circle class="title-disc" cx="345" cy="153" r="659" fill="var(--slate)"/>
    <circle class="title-ring" cx="360" cy="140" r="626" fill="none" stroke="url(#goldRing)" stroke-width="8"/>

    <text class="title-line" x="58" y="252" font-size="224" textLength="784" lengthAdjust="spacingAndGlyphs" fill="url(#goldText)">PROPERTY</text>
    <text class="title-line" x="48" y="446" font-size="224" textLength="806" lengthAdjust="spacingAndGlyphs" fill="url(#goldText)">AUCTIONS</text>
    <text class="host-name" x="48" y="580" font-size="88" textLength="644" lengthAdjust="spacingAndGlyphs">TEODOR BRAMWICK</text>
  </svg>
</main>
</body>
</html>
```